Tovaberry LLC website and online trading portal

Beverage Manufacturing company needs a website design. Should include 5 main pages. Home, Products, About, FAQ and Contact Us. Should also include a shopping cart, online order and shipping page. Company logo is attached.

Target Market(s)

General Public, health conscious individuals

Font styles to use
Serif
Sans Serif
Script

Colors
abd037
fbee3e
ffc214
ffffff

Requirements
Must have
• e-commerce site with 5 main pages. Home, Products, About, FAQ and Contact Us. Should also include a shopping cart, online order and shipping page. Coloscheme should be derived from attached logo

```html
<!DOCTYPE html>
<html lang="en">
<head>
<meta charset="utf-8">
<title>Tovaberry – Website & Product Page</title>
<link href="https://fonts.googleapis.com/css2?family=Inter:wght@400;500;600;700;800&family=Archivo+Black&family=Anton&display=swap" rel="stylesheet">
<style>
:root{
  --green:#abd037;
  --lemon:#fbee3e;
  --amber:#ffc214;
  --white:#ffffff;
  --cream:#fdf5c4;
  --leaf:#14cc6e;
  --ink:#111111;
  --charcoal:#2a2c30;
  --mist:#efefef;
  --forest:#2f4a1a;
}
*{margin:0;padding:0;box-sizing:border-box}
html,body{width:1200px;height:1200px;overflow:hidden}
body{position:relative;background:var(--cream);font-family:"Inter",sans-serif;color:var(--ink)}
.backdrop{position:absolute;inset:0}
.abs{position:absolute}

/* website page */
.site{position:absolute;left:69px;top:96px;width:480px;height:1104px;background:var(--white);overflow:hidden;border-top:3px solid #e8e8e8}
.brand{left:47px;top:11px;width:38px;height:38px;border-radius:50%;background:var(--green)}
.brand-name{left:90px;top:24px;font-size:9px;font-weight:700;color:var(--green)}
.nav a{position:absolute;top:22px;font-size:7px;font-weight:600;color:var(--ink);text-decoration:none}
.hero-title{left:53px;top:92px;width:240px;text-align:center;font-size:19.5px;font-weight:600;line-height:22px;letter-spacing:-.2px}
.heart{left:103px;top:154px;width:22px;height:22px;border-radius:50%;background:var(--green);display:flex;align-items:center;justify-content:center}
.pill{display:flex;align-items:center;justify-content:center;gap:6px;background:var(--white);border-radius:20px;box-shadow:0 2px 5px rgba(0,0,0,.18);font-weight:500}
.order{left:137px;top:153px;width:88px;height:22px;font-size:8px}
.photo-bottle{border-radius:14px 14px 4px 4px;background:linear-gradient(180deg,#f6e9b8 0%,#ffc214 30%,#f0a90e 60%,#f5dd8c 100%)}
.hero-bottle{left:340px;top:43px;width:74px;height:202px;border-radius:20px 20px 4px 4px}

.bands{left:0;top:245px;width:480px;height:132px;display:flex}
.band{position:relative;flex:1;overflow:hidden;color:var(--white)}
.band.green{background:var(--green)}
.band.lemon{background:var(--lemon)}
.band.amber{background:var(--amber)}
.band-head{font-family:"Archivo Black",sans-serif;font-size:8.5px;line-height:10px;letter-spacing:.3px}
.band-body{font-size:7.2px;line-height:8.8px;font-weight:500}
.pineapple{background:linear-gradient(180deg,#6f8f3a 0%,#8a7a2c 40%,#b37d1c 100%);border-radius:40% 40% 30% 30%}

.benefit-bottle{left:79px;top:449px;width:41px;height:144px}
.benefit-title{left:205px;top:442px;font-size:11.6px;font-weight:600;line-height:15px}
.benefit-copy{left:205px;top:485px;width:200px;font-size:4.9px;line-height:7.9px;color:#222}
.benefit-copy p{margin-bottom:7.9px}
.divider{left:0;top:629px;width:480px;height:14px;background:var(--mist)}

.reviews-title{left:0;top:671px;width:480px;text-align:center;font-size:11px;font-weight:600}
.reviews-sub{left:180px;top:693px;width:120px;text-align:center;font-size:3.2px;line-height:5.5px;color:#333}
.review{width:111px;height:31px;top:736px;background:var(--white);border-radius:4px;box-shadow:0 1px 4px rgba(0,0,0,.15)}
.avatar{width:26px;height:26px;border-radius:50%;background:linear-gradient(135deg,#b9b9b9,#6b6b6b);border:1.5px solid var(--white);box-shadow:0 1px 3px rgba(0,0,0,.2)}
.review-name{font-size:6.8px;font-weight:600}
.review-text{font-size:3px;line-height:4.8px;color:#333;width:80px}
.dot{width:5px;height:5px;border-radius:50%;background:var(--green)}
.dot.hollow{background:var(--white);border:1.2px solid var(--green)}

.poster{top:833px;width:105px;height:149px;background:radial-gradient(ellipse at 55% 45%,#7a6a22 0%,#3e5a22 40%,var(--forest) 100%);box-shadow:0 2px 5px rgba(0,0,0,.35);display:flex;align-items:center;justify-content:center;text-align:center}
.poster span{font-family:"Anton",sans-serif;color:var(--white);font-size:16px;line-height:16.5px;letter-spacing:-.2px}

.footer{left:0;top:1019px;width:480px;height:60px;background:var(--lemon)}
.footer-head{font-size:7px;font-weight:700;letter-spacing:.5px}
.footer-small{font-size:5px;line-height:6.6px;color:#222}
.social{width:10px;height:10px;border-radius:2.5px;background:var(--ink)}
.legal{left:0;top:1079px;width:480px;height:25px;background:var(--charcoal)}
.legal a{position:absolute;top:9px;font-size:6px;font-weight:600;color:var(--white);text-decoration:none}

/* product page */
.label{left:1028px;top:278px;font-family:"Inter",sans-serif;font-size:23px;font-weight:800;letter-spacing:-.3px}
.product{left:587px;top:326px;width:640px;height:474px;background:var(--white);border-radius:32px;box-shadow:0 2px 3px rgba(0,0,0,.12)}
.gallery{left:34px;top:59px;width:225px;height:307px;border-radius:11px;background:var(--white);box-shadow:0 1px 5px rgba(0,0,0,.2)}
.halo{left:29px;top:36px;width:166px;height:166px;border-radius:50%;background:var(--lemon)}
.gallery-bottle{left:86px;top:58px;width:51px;height:178px}
.crumb{left:307px;top:32px;font-size:5.6px;font-weight:500}
.product-title{left:307px;top:49px;font-family:"Archivo Black",sans-serif;font-size:21.5px;line-height:23px;color:var(--green)}
.product-desc{left:307px;top:110px;font-size:7px;line-height:11px;letter-spacing:.35px;color:#222}
.price{left:310px;top:170px;font-family:"Archivo Black",sans-serif;font-size:14px;letter-spacing:.6px}
.cart{left:400px;top:166px;width:114px;height:27px;font-size:11px;letter-spacing:.3px;gap:8px}
.tabs{left:307px;top:238px;width:255px;height:32px;border-radius:16px;background:var(--white);box-shadow:0 1px 4px rgba(0,0,0,.08);display:flex}
.tab{flex:1;display:flex;align-items:center;justify-content:center;font-size:9.5px;font-weight:600;border-radius:16px}
.tab.active{flex:0 0 119px;background:var(--lemon);box-shadow:0 2px 4px rgba(0,0,0,.12)}
.product-copy{left:310px;top:304px;width:228px;font-size:8.6px;line-height:11.6px;color:#222}
</style>
</head>
<body>

<svg class="backdrop" width="1200" height="1200" viewBox="0 0 1200 1200" aria-hidden="true">
  <path d="M0 0 H342 L560 200 C610 240 648 290 668 330 L662 730 L549 735 L69 600 L0 535 Z" fill="var(--leaf)"/>
</svg>

<div class="site">
  <div class="abs brand"></div>
  <div class="abs brand-name">Tovaberry</div>
  <nav class="nav">
    <a style="left:140px">HOME</a>
    <a style="left:177px">PRODUCTS</a>
    <a style="left:232px">ABOUT</a>
    <a style="left:273px">CONTACT US</a>
    <a style="left:335px">FAQ</a>
    <a style="left:368px">SHOP NOW</a>
  </nav>

  <h1 class="abs hero-title">All the healthy benefits and a delicious taste</h1>
  <div class="abs heart">
    <svg width="10" height="9" viewBox="0 0 24 22"><path d="M12 20 C4 14 1 10 1 6.5 A5.5 5.5 0 0 1 12 4 A5.5 5.5 0 0 1 23 6.5 C23 10 20 14 12 20Z" fill="none" stroke="#111" stroke-width="2.4"/></svg>
  </div>
  <div class="abs pill order">
    <svg width="9" height="8" viewBox="0 0 24 22"><path d="M1 2h4l3 12h12l3-9H7" fill="none" stroke="#111" stroke-width="2.2"/><circle cx="10" cy="19" r="1.8" fill="#111"/><circle cx="18" cy="19" r="1.8" fill="#111"/></svg>
    Order Now
  </div>
  <div class="abs photo-bottle hero-bottle" role="img" aria-label="Bottle of ginger pineapple juice"></div>

  <div class="abs bands">
    <div class="band green">
      <div class="abs band-head" style="left:0;top:28px;width:160px;text-align:center">REDUCE STRESS AND<br>RELIEF MUSCLE PAIN</div>
      <div class="abs photo-bottle" style="left:50px;top:50px;width:58px;height:82px" role="img" aria-label="Three juice bottles"></div>
    </div>
    <div class="band lemon">
      <div class="abs band-head" style="left:12px;top:34px">HEART HEALTHY</div>
      <div class="abs band-body" style="left:12px;top:55px;width:80px">CONTAINS GINGEROLS. May improve circulation and guard against heart attacks.</div>
      <div class="abs photo-bottle" style="left:105px;top:52px;width:26px;height:80px" role="img" aria-label="Juice bottle"></div>
    </div>
    <div class="band amber">
      <div class="abs band-body" style="left:12px;top:22px;width:90px;font-size:8.4px;line-height:10.3px">Pineapple contains high level of Bromelain</div>
      <div class="abs pineapple" style="left:75px;top:38px;width:44px;height:96px" role="img" aria-label="Whole pineapple"></div>
    </div>
  </div>

  <div class="abs photo-bottle benefit-bottle" role="img" aria-label="Bottle of ginger pineapple juice"></div>
  <h2 class="abs benefit-title">Health Benefits of Ginger, Pineapple<br>and Cloves</h2>
  <div class="abs benefit-copy">
    <p>Anti-inflammatory and Antibacterial. Reduce oxidative stress. high in Antioxidants<br>and Vitamin C.<br>Maintain / Enhance Male Virility.<br>Help in relieving Muscle pain and Lowering LDL Cholesterol. Immune system<br>booster, Rich source if Manganese, Dietary Fiber and Thiamin.</p>
    <p>Pineapple contains high levels of Bromelain, an enzyme used for<br>reducing inflammation, ulcerative colitis, debridement, pulmonary<br>edema and helping the body get rid of fat.</p>
    <p>Heart Healthy-Contains gingerols. May improve circulation and guard against<br>hearth attacks.<br>Can improve liver function.<br>Antiviral properties can help reduce symptoms of colds and flu.</p>
  </div>
  <div class="abs divider"></div>

  <h2 class="abs reviews-title">What Our Customers Says</h2>
  <p class="abs reviews-sub">Some of our Regular Customers and Buyers reached out to us and gave some awesome feedback. See what they have to tell about us.</p>

  <div class="abs review" style="left:37px"></div>
  <div class="abs avatar" role="img" aria-label="Customer portrait" style="left:27px;top:732px"></div>
  <div class="abs review-name" style="left:60px;top:741px">Mara Ellison</div>
  <div class="abs review-text" style="left:60px;top:751px">Really loved the Flavour and taste. It helps me keep healthy on a daily basis.</div>

  <div class="abs review" style="left:190px"></div>
  <div class="abs avatar" role="img" aria-label="Customer portrait" style="left:179px;top:732px"></div>
  <div class="abs review-name" style="left:212px;top:741px">Tobin Reyes</div>
  <div class="abs review-text" style="left:212px;top:751px">Really loved the Flavour and taste. It helps me keep healthy on a daily basis.</div>

  <div class="abs review" style="left:343px"></div>
  <div class="abs avatar" role="img" aria-label="Customer portrait" style="left:332px;top:731px"></div>
  <div class="abs review-name" style="left:365px;top:740px">Arlo Bennett</div>
  <div class="abs review-text" style="left:365px;top:750px">Really loved the Flavour and taste. It helps me keep healthy on a daily basis.</div>

  <div class="abs dot" style="left:222px;top:795px"></div>
  <div class="abs dot" style="left:232px;top:795px"></div>
  <div class="abs dot hollow" style="left:242px;top:795px"></div>
  <div class="abs dot" style="left:252px;top:795px"></div>

  <div class="abs poster" style="left:42px" role="img" aria-label="Promotional poster with juice bottle, ginger and pineapple"><span>BUY ONLINE</span></div>
  <div class="abs poster" style="left:187px" role="img" aria-label="Promotional poster with juice bottle, ginger and pineapple"><span>EXPLORE<br>PRODUCTS</span></div>
  <div class="abs poster" style="left:332px" role="img" aria-label="Promotional poster with juice bottle, ginger and pineapple"><span>ABOUT<br>TOVABERRY</span></div>

  <footer class="abs footer">
    <div class="abs footer-head" style="left:39px;top:17px">CONNECT WITH US</div>
    <div class="abs social" style="left:42px;top:34px"></div>
    <div class="abs social" style="left:67px;top:34px"></div>
    <div class="abs social" style="left:91px;top:34px"></div>
    <div class="abs social" style="left:116px;top:34px;border-radius:50%"></div>
    <div class="abs footer-head" style="left:191px;top:17px">OTHER LINKS</div>
    <div class="abs footer-small" style="left:191px;top:30px">Write to us<br>Blogs<br>Our Stores</div>
    <div class="abs footer-head" style="left:337px;top:17px">MANUFACTURED BY</div>
    <div class="abs footer-small" style="left:337px;top:30px">Tovaberry LLC<br>212 Orchard Lane,<br>Suite B, Millbrook GA 30000</div>
  </footer>
  <div class="abs legal">
    <a style="left:42px">Home</a>
    <a style="left:72px">About</a>
    <a style="left:103px">FAQ</a>
    <a style="left:129px">Contact Us</a>
    <a style="left:289px">Terms of use</a>
    <a style="left:348px">Privacy</a>
    <a style="left:392px">All rights Reserved.</a>
  </div>
</div>

<div class="abs label">Product page</div>

<section class="abs product">
  <div class="abs gallery">
    <div class="abs halo"></div>
    <div class="abs photo-bottle gallery-bottle" role="img" aria-label="Bottle of ginger pineapple juice"></div>
    <div class="abs dot" style="left:92px;top:273px;width:7px;height:7px"></div>
    <div class="abs dot" style="left:106px;top:273px;width:7px;height:7px"></div>
    <div class="abs dot hollow" style="left:119px;top:273px;width:7px;height:7px"></div>
    <div class="abs dot" style="left:132px;top:273px;width:7px;height:7px"></div>
  </div>
  <div class="abs crumb">Home &gt; Product</div>
  <h1 class="abs product-title">Ginger Pineapple<br>Juice</h1>
  <p class="abs product-desc">The Goodness of Ginger and the taste if Pineapple and cloves<br>makes the Tovaberry Healthy and Tasty drink.</p>
  <div class="abs price">$ 7.00</div>
  <div class="abs pill cart">
    <svg width="12" height="11" viewBox="0 0 24 22"><path d="M1 2h4l3 12h12l3-9H7" fill="none" stroke="#111" stroke-width="2.2"/><circle cx="10" cy="19" r="1.8" fill="#111"/><circle cx="18" cy="19" r="1.8" fill="#111"/></svg>
    Add to Cart
  </div>
  <div class="abs tabs">
    <div class="tab active">Details</div>
    <div class="tab">Ingredaients</div>
  </div>
  <p class="abs product-copy">Anti-inflammatory and Antibacterial. Reduce oxidative stress. high in Antioxidants and Vitamin C.<br>Maintain / Enhance Male Virility.<br>Help in relieving Muscle pain and Lowering LDL Cholesterol. Immune system booster, Rich source if Manganese, Dietary Fiber and Thiamin.<br>Pineapple contains high levels of Bromelain, an enzyme used for<br>reducing inflammation, ulcerative colitis, debridement, pulmonary<br>edema and helping the body get rid of fat.</p>
</section>

</body>
</html>
```